Update the A4 Specials Page for Restaurant/Cafe

Provide a MINIMALIST attractive Specials page we can print weekly for our food and drink specials to give to our guests. Final design is to be provided in WORD Document so it can be easily edited by Manager. Should be black text and MINIMALIST to minimise ink usage as we print hundreds a week. We have UPLOADED the existing page as a template for you to update. Maybe logo can stay, see what you think. Or delete it and do something else. Keep it simple. Choose a good FONT. Could be a little playful with a cocktail ICON or something. Our existing menus can be seen at www.tallowmillcafe.com.au and they are using font Alegreya. Please note we are unable to provide any feedback to designers, however we really do appreciate your time if you are submitting a design. Thank you for your participation.

```html
<!DOCTYPE html>
<html lang="en">
<head>
<meta charset="utf-8">
<title>Tallow Mill Cafe – Weekly Specials</title>
<link rel="stylesheet" href="https://fonts.googleapis.com/css2?family=Italiana&family=Alegreya+SC:wght@700&family=Poppins:wght@400;600;700&display=swap">
<style>
  :root {
    --backdrop: #e7e5e1;
    --paper: #ffffff;
    --teal: #2e5a5e;
    --ink: #222222;
    --ghost: #f1f2f2;
  }
  * { margin: 0; padding: 0; box-sizing: border-box; }
  html, body {
    width: 800px; height: 1200px; overflow: hidden;
    background: var(--backdrop);
  }
  .sheet {
    position: absolute; left: 0; top: 35px;
    width: 992px; height: 1402px;
    background: var(--paper);
    transform: scale(0.8065); transform-origin: top left;
    box-shadow: 0 2px 10px rgba(0,0,0,0.12);
    color: var(--ink);
    font-family: "Poppins", sans-serif;
  }
  .frames { position: absolute; inset: 0; }
  .frames path { fill: none; stroke: var(--teal); stroke-width: 2; }
  .motif { position: absolute; background: var(--ghost); border-radius: 10px; }
  .corner-mark { position: absolute; width: 40px; height: 40px; background: var(--teal); border-radius: 50% 0 50% 50%; opacity: .9; }
  .brand {
    position: absolute; left: 361px; top: 120px; width: 270px; height: 134px;
    background: var(--teal); color: #fff;
    display: flex; flex-direction: column; align-items: center; justify-content: center;
    font-family: "Poppins", sans-serif; font-weight: 700;
    font-size: 34px; line-height: 1.05; letter-spacing: 1px; text-align: center;
  }
  .c { position: absolute; left: 0; width: 992px; text-align: center; transform: translateY(-50%); white-space: nowrap; }
  .section-title { font-family: "Italiana", sans-serif; font-size: 60px; color: var(--ink); }
  .section-title.caps { font-size: 58px; }
  .item-name { font-family: "Alegreya SC", serif; font-weight: 700; font-size: 29px; letter-spacing: 3px; color: var(--teal); }
  .item-lead { font-weight: 600; font-size: 18px; }
  .item-note { font-weight: 400; font-size: 17px; }
  .item-tag { font-weight: 600; font-size: 16px; }
  .price { font-weight: 700; font-size: 38px; color: var(--teal); }
  .price span { font-weight: 400; }
</style>
</head>
<body>
<main class="sheet">
  <svg class="frames" width="992" height="1402" viewBox="0 0 992 1402" aria-hidden="true">
    <path d="M97,155 A82,82 0 0 0 179,73 L813,73 A82,82 0 0 0 895,155 L895,303 L97,303 Z"/>
    <path d="M237,372 L97,372 L97,709 L895,709 L895,372 L755,372"/>
    <path d="M237,785 L97,785 L97,1252 A82,82 0 0 1 179,1334 L813,1334 A82,82 0 0 1 895,1252 L895,785 L755,785"/>
  </svg>

  <div class="corner-mark" style="left:97px;top:73px" role="img" aria-label="Small leaf corner ornament"></div>
  <div class="corner-mark" style="left:855px;top:73px;transform:scaleX(-1)" role="img" aria-label="Small leaf corner ornament"></div>
  <div class="corner-mark" style="left:97px;top:1294px;transform:scaleY(-1)" role="img" aria-label="Small leaf corner ornament"></div>
  <div class="corner-mark" style="left:855px;top:1294px;transform:scale(-1,-1)" role="img" aria-label="Small leaf corner ornament"></div>

  <div class="motif" style="left:99px;top:374px;width:133px;height:133px" role="img" aria-label="Faint line drawing of a grill pan"></div>
  <div class="motif" style="left:672px;top:497px;width:221px;height:210px" role="img" aria-label="Faint line drawing of a ladle over a soup bowl"></div>
  <div class="motif" style="left:99px;top:787px;width:133px;height:225px" role="img" aria-label="Faint line drawing of a cocktail glass with fruit"></div>
  <div class="motif" style="left:672px;top:1087px;width:180px;height:245px" role="img" aria-label="Faint line drawing of a beer glass"></div>

  <div class="brand">TALLOW MILL<br>CAFE</div>

  <h1 class="c section-title caps" style="top:372px">WEEKLY SPECIALS</h1>

  <h2 class="c item-name" style="top:435px">CHICKEN FILO</h2>
  <p class="c item-lead" style="top:468px">Creamy Chicken with Pinenuts, wrapped in Filo Pastry.</p>
  <p class="c item-note" style="top:494px">Served with Side Salad &amp; Zulu Sauce</p>
  <p class="c price" style="top:529px"><span>$</span>24</p>

  <h2 class="c item-name" style="top:592px">MINESTRONE SOUP</h2>
  <p class="c item-lead" style="top:626px">Served with Garlic Bread</p>
  <p class="c price" style="top:663px"><span>$</span>8</p>

  <h1 class="c section-title" style="top:787px;font-size:68px">Cocktail Special</h1>
  <h2 class="c item-name" style="top:854px">PASSIONISTA</h2>
  <p class="c item-lead" style="top:896px">Vodka, Passionfruit Pulp, Mango Puree</p>
  <p class="c item-note" style="top:922px">Top up with Ginger &amp; Lemon Kombucha</p>
  <p class="c price" style="top:961px"><span>$</span>17</p>

  <h1 class="c section-title" style="top:1047px;font-size:68px">Craft Beer Special</h1>
  <h2 class="c item-name" style="top:1120px">COPPER GECKO</h2>
  <p class="c item-tag" style="top:1147px">SUN PARADE</p>
  <p class="c item-note" style="top:1173px">Tropical Pale Ale</p>
  <p class="c item-note" style="top:1198px">4.8% Alc.</p>
  <p class="c price" style="top:1238px"><span>$</span>10</p>
</main>
</body>
</html>
```